Your best Design

Show me your best.

Target Market(s)

Show me your best.

Requirements
Must have
• Show me your best.
Nice to have
• Show me your best.
Should not have
• Show me your best.

```html
<!DOCTYPE html>
<html lang="en">
<head>
<meta charset="utf-8">
<title>The Chinese Property Essential Buyers Guide</title>
<link href="https://fonts.googleapis.com/css2?family=Open+Sans:wght@300;400;600&display=swap" rel="stylesheet">
<style>
  :root {
    --stage: #e9e6ee;
    --purple-deep: #4a2383;
    --purple-mid: #5e3299;
    --band-line: #b9a3dc;
    --tile-border: #d9cfe8;
    --white: #ffffff;
  }
  * { margin: 0; padding: 0; box-sizing: border-box; }
  html, body { width: 1200px; height: 854px; overflow: hidden; }
  body {
    background: var(--stage);
    font-family: "Open Sans", sans-serif;
    position: relative;
  }
  .cover {
    position: absolute;
    left: 315px; top: 27px;
    width: 570px; height: 800px;
    background: linear-gradient(160deg, var(--purple-mid) 0%, var(--purple-deep) 70%);
    overflow: hidden;
    box-shadow: 0 6px 22px rgba(40, 20, 70, .28);
  }
  .cover-shapes { position: absolute; inset: 0; }
  .title {
    position: absolute;
    right: 28px; top: 58px;
    width: 360px;
    color: var(--white);
    font-weight: 300;
    line-height: 1;
    white-space: nowrap;
  }
  .title-the { display: block; font-size: 20px; margin-left: 14px; }
  .title-subject { display: block; font-size: 34px; margin-top: 4px; margin-left: 14px; }
  .title-essential { display: block; font-size: 20px; text-align: right; margin-top: 2px; }
  .title-main { display: block; font-size: 58px; margin-top: 2px; letter-spacing: -0.5px; text-align: right; }
  .quote-mark {
    position: absolute;
    color: var(--white);
    font-family: Georgia, serif;
    font-size: 70px;
    line-height: 1;
  }
  .quote-open { left: 140px; top: 172px; }
  .quote-close { left: 372px; top: 598px; }
  .portrait-grid { position: absolute; inset: 0; }
  .portrait {
    position: absolute;
    width: 130px; height: 92px;
    border: 3px solid var(--tile-border);
    box-shadow: 0 2px 6px rgba(20, 5, 40, .45);
    transform: rotate(-26deg);
  }
  .tone-a { background: linear-gradient(135deg, #8fb6d8, #5a6f8a); }
  .tone-b { background: linear-gradient(135deg, #c9c9cf, #8a8f9c); }
  .tone-c { background: linear-gradient(135deg, #a9bcd0, #3f4b60); }
  .tone-d { background: linear-gradient(135deg, #c7444f, #7a2a3e); }
  .tone-e { background: linear-gradient(135deg, #e8e8e8, #5c5c5c); }
  .tone-f { background: linear-gradient(135deg, #c4a75a, #6b5a3a); }
  .tone-g { background: linear-gradient(135deg, #d2c6a8, #6f6a5c); }
  .tone-h { background: linear-gradient(135deg, #3a3a3e, #b8442f); }
  .tone-i { background: linear-gradient(135deg, #b03a3a, #4a3c5c); }
  .price {
    position: absolute;
    left: 8px; top: 500px;
    transform-origin: left top;
    transform: rotate(90deg) translate(0, -30px);
    color: var(--white);
    font-size: 15px;
    font-weight: 400;
    letter-spacing: 1px;
    white-space: nowrap;
  }
  .price sup { font-size: 9px; }
</style>
</head>
<body>
  <main class="cover">
    <svg class="cover-shapes" width="570" height="800" viewBox="0 0 570 800" aria-hidden="true">
      <defs>
        <linearGradient id="band" x1="0" y1="0" x2="0" y2="1">
          <stop offset="0" stop-color="#8a63c4"/>
          <stop offset="1" stop-color="#6a3fa6"/>
        </linearGradient>
        <linearGradient id="dusk" x1="0" y1="0" x2="0" y2="1">
          <stop offset="0" stop-color="#8e76c9"/>
          <stop offset="0.45" stop-color="#6b4fa6"/>
          <stop offset="1" stop-color="#2f2350"/>
        </linearGradient>
      </defs>
      <path class="top-band" d="M0 0 H570 V40 H260 L235 62 H0 Z" fill="url(#band)"/>
      <path d="M0 58 H232 L256 36 H570" fill="none" stroke="#b9a3dc" stroke-width="1.5"/>
      <path class="city-frame" d="M0 450 H130 L165 415 L200 450 H300 V800 H0 Z"
            fill="url(#dusk)" role="img" aria-label="Photograph of a modern city skyline with tall towers reflected in a park lake at dusk"/>
      <path d="M0 444 H128 L165 408 L202 444 H306 V800" fill="none" stroke="#b9a3dc" stroke-width="1.5"/>
      <rect x="0" y="470" width="32" height="150" fill="#5a3a94" opacity=".85"/>
    </svg>

    <h1 class="title">
      <span class="title-the">The</span>
      <span class="title-subject">Chinese Property</span>
      <span class="title-essential">Essential</span>
      <span class="title-main">Buyers Guide</span>
    </h1>

    <span class="quote-mark quote-open">&#8220;</span>

    <div class="portrait-grid">
      <div class="portrait tone-a" style="left:25px; top:244px;" role="img" aria-label="Portrait photograph of a property investor"></div>
      <div class="portrait tone-b" style="left:128px; top:246px;" role="img" aria-label="Portrait photograph of a business leader"></div>
      <div class="portrait tone-d" style="left:231px; top:258px;" role="img" aria-label="Portrait photograph of an actress"></div>
      <div class="portrait tone-e" style="left:361px; top:268px;" role="img" aria-label="Black and white portrait photograph of a technology founder"></div>
      <div class="portrait tone-c" style="left:77px; top:349px;" role="img" aria-label="Portrait photograph of an entrepreneur"></div>
      <div class="portrait tone-f" style="left:170px; top:366px;" role="img" aria-label="Portrait photograph of a business leader"></div>
      <div class="portrait tone-h" style="left:295px; top:379px;" role="img" aria-label="Portrait photograph of an actor at an event"></div>
      <div class="portrait tone-g" style="left:126px; top:485px;" role="img" aria-label="Portrait photograph of a mining investor"></div>
      <div class="portrait tone-i" style="left:226px; top:504px;" role="img" aria-label="Portrait photograph of an internet entrepreneur"></div>
    </div>

    <span class="quote-mark quote-close">&#8221;</span>

    <p class="price">AUD $ 18.<sup>00</sup></p>
  </main>
</body>
</html>
```